Banner for construction site to identify developer

we need a 4 foot by 8 foot banner to hang on the fence of a residential townhome development in Phoenix, Arizona that identifies Tollen Ridge as the company behind the development/project. Also needs to include the logo, phone number, and web address. Would like to stick with the blue colors provided in the attached logo. The blues should stay the same but the letters in the logo can change to another color if necessary. Feel free to use "Tollen Ridge" in place of "Tollen Ridge Group". Looking for use of colors/design to take up space so banner is not just text with a logo.

Target Market(s)

drive by traffic looking at the site

Industry/Entity Type

Real Estate

Colors
0054AA
0677BA
7BADD7
CADEEF
E8F1F8

Requirements
Must have
• company name, phone number and web address

```html
<!DOCTYPE html>
<html lang="en">
<head>
<meta charset="utf-8">
<title>Tollen Ridge – Site Banner</title>
<link href="https://fonts.googleapis.com/css2?family=Open+Sans:wght@400;600;700;800&display=swap" rel="stylesheet">
<style>
  :root {
    --backdrop: #c6c9cc;
    --navy: #1c2236;
    --navy-mid: #272e46;
    --cyan: #1da6dc;
    --steel-blue: #1f6fa3;
    --ink: #2e2f36;
    --white: #ffffff;
  }
  html, body {
    margin: 0;
    padding: 0;
    width: 1111px;
    height: 1200px;
    overflow: hidden;
    background: var(--backdrop);
    font-family: "Open Sans", Arial, sans-serif;
  }
  .banner {
    position: absolute;
    left: 55px;
    top: 350px;
    width: 1000px;
    height: 500px;
    background: var(--white);
    box-shadow: 0 10px 18px rgba(0,0,0,0.35);
    overflow: hidden;
  }
  .hero {
    position: absolute;
    left: 0; top: 0;
    width: 1000px;
    height: 287px;
  }
  .hero-photo {
    position: absolute;
    inset: 0;
    background: linear-gradient(90deg, var(--navy) 0%, var(--navy-mid) 45%, #2f3850 60%, #c9bcaf 72%, #e8e1d8 84%, #b5a598 92%, #3c5a60 100%);
  }
  .headline {
    position: absolute;
    left: 55px;
    top: 38px;
    margin: 0;
    font-size: 80px;
    font-weight: 800;
    line-height: 1;
    letter-spacing: 0.5px;
    color: var(--cyan);
  }
  .tagline {
    position: absolute;
    left: 57px;
    top: 140px;
    margin: 0;
    color: var(--white);
    font-size: 32px;
    line-height: 39px;
    text-transform: uppercase;
  }
  .tagline .light { font-weight: 400; display: block; }
  .tagline .strong { font-weight: 800; display: block; }
  .accent-stripe {
    position: absolute;
    left: 0; top: 287px;
    width: 1000px;
    height: 10px;
    background: var(--cyan);
  }
  .accent-tab {
    position: absolute;
    left: 0; top: 296px;
  }
  .brand-name {
    position: absolute;
    left: 55px;
    top: 372px;
    margin: 0;
    color: var(--ink);
    font-size: 42px;
    font-weight: 700;
    line-height: 1;
    white-space: nowrap;
  }
  .contact-phone {
    position: absolute;
    left: 499px;
    top: 330px;
    display: flex;
    align-items: center;
    gap: 9px;
    color: var(--ink);
    font-size: 50px;
    font-weight: 700;
    line-height: 1;
  }
  .contact-web {
    position: absolute;
    left: 499px;
    top: 390px;
    width: 501px;
    height: 48px;
    background: var(--steel-blue);
    color: var(--white);
    font-size: 29px;
    line-height: 48px;
    padding-left: 18px;
    box-sizing: border-box;
  }
  .contact-web .domain { font-weight: 700; }
</style>
</head>
<body>
  <main class="banner">
    <section class="hero">
      <div class="hero-photo" role="img" aria-label="Photo of a modern multi-storey residential building with balconies against a dusk city skyline"></div>
      <h1 class="headline">TOLLEN RIDGE</h1>
      <p class="tagline">
        <span class="light">Crafting Phoenix's</span>
        <span class="strong">Premium Residential</span>
        <span class="strong">Townhomes.</span>
      </p>
    </section>

    <div class="accent-stripe"></div>
    <svg class="accent-tab" width="1000" height="40" viewBox="0 0 1000 40" aria-hidden="true">
      <polygon points="145,0 469,0 432,38 187,38" fill="var(--cyan)"/>
    </svg>

    <p class="brand-name">Tollen Ridge Group</p>

    <div class="contact-phone">
      <svg width="41" height="41" viewBox="0 0 40 40" aria-hidden="true">
        <circle cx="20" cy="20" r="20" fill="var(--cyan)"/>
        <path d="M14.5 10.5c1-.6 2.1-.3 2.7.6l2 3.2c.5.9.3 2-.5 2.6l-1.4 1c.9 2.1 2.6 3.9 4.7 4.9l1.1-1.4c.6-.8 1.7-1 2.6-.4l3.1 2.1c.9.6 1.1 1.8.5 2.7l-1.1 1.6c-.8 1.1-2.2 1.6-3.5 1.2-5.5-1.7-9.8-6.1-11.4-11.6-.4-1.3.1-2.7 1.2-3.5z" fill="var(--white)"/>
      </svg>
      <span>(480)-555-0147</span>
    </div>

    <div class="contact-web">www.<span class="domain">tollenridgegroup</span>.com</div>
  </main>
</body>
</html>
```